Lumavorne Business Card Design

I need a business card design for a new Business, that is focused on Custom Made Designer Furniture. that is aimed at the mid to high end markets. I would like a card that would in some way portray what I do for my clients in the way we are able to make any idea a reality and also work within a set budget to meet their requirements.
I like quite contemporary colours and styling and I want the final design to communicate a Contemporary and Professional image.

Target Market(s)

mid to high end market

Industry/Entity Type

Business

Contact Information for Business Card

Lumavorne
Harold Brenning
82 Wendle Ave, Tarrow, Auckland, New Zealand 0927.

Requirements
Nice to have
• I would also like to utilize the spot gloss or raised print on my cards

```html
<!DOCTYPE html>
<html lang="en">
<head>
<meta charset="utf-8">
<title>Lumavorne — Business Card</title>
<link rel="stylesheet" href="https://fonts.googleapis.com/css2?family=Poiret+One&display=swap">
<style>
  :root {
    --paper: #ffffff;
    --ink: #000000;
    --band-text: #ffffff;
    --font-main: "Poiret One", sans-serif;
  }
  * { box-sizing: border-box; margin: 0; padding: 0; }
  html, body {
    width: 1200px;
    height: 741px;
    overflow: hidden;
    background: var(--paper);
  }
  .card {
    position: relative;
    width: 1200px;
    height: 741px;
    background: var(--paper);
    color: var(--ink);
    font-family: var(--font-main);
  }
  .brand {
    position: absolute;
    left: 0;
    top: 200px;
    width: 100%;
    text-align: center;
    font-size: 92px;
    line-height: 1;
    font-weight: 400;
    color: var(--ink);
    letter-spacing: 2px;
  }
  .holder {
    position: absolute;
    left: 0;
    top: 370px;
    width: 100%;
    text-align: center;
  }
  .holder-name {
    font-size: 52px;
    line-height: 1;
    font-weight: 400;
    letter-spacing: 1px;
  }
  .holder-role {
    font-size: 29px;
    line-height: 1;
    margin-top: 4px;
    letter-spacing: 1px;
  }
  .address-band {
    position: absolute;
    left: 24px;
    top: 544px;
    width: 1159px;
    height: 88px;
    background: var(--ink);
    color: var(--band-text);
    display: flex;
    align-items: center;
    justify-content: center;
  }
  .address {
    font-size: 29px;
    letter-spacing: 1.5px;
    font-style: normal;
  }
</style>
</head>
<body>
  <main class="card">
    <h1 class="brand">Lumavorne</h1>
    <section class="holder">
      <p class="holder-name">Harold Brenning</p>
      <p class="holder-role">manager</p>
    </section>
    <div class="address-band">
      <address class="address">82 Wendle Ave, Tarrow, Auckland, New Zealand 0927</address>
    </div>
  </main>
</body>
</html>
```